Penny auctions banner design to get people to sign up

Show the 3 steps needed to get started bidding with penny auctions on my website ZelNork.com. The core colors should be black, grey, and yellow.

It needs to show the following steps: 1) Register an account. 2) Purchase the starter package. 3) Start bidding and save up to 98% off!

Some creativity would be good so if you have some better ideas then please let them flow and show me your best banner design :) Thank you! Comment with any questions you have. Attached is my logo.

```html
<!DOCTYPE html>
<html lang="en">
<head>
<meta charset="utf-8">
<title>ZelNork.com – Get started in 3 steps</title>
<link rel="stylesheet" href="https://fonts.googleapis.com/css2?family=Oswald:wght@500;600&display=swap">
<style>
  :root {
    --bg-dark: #3d3d3d;
    --panel-dark: #4b4b4b;
    --panel-mid: #5a5a5a;
    --floor: #9a9a9a;
    --floor-light: #b4b4b4;
    --yellow: #e9c12b;
    --yellow-deep: #cfa514;
    --yellow-light: #f4d561;
    --cube-front: #262626;
    --cube-top: #3a3a3a;
    --cube-side: #1b1b1b;
    --number: #8d8d8d;
    --text-light: #f2f2f2;
    --text-dark: #161616;
  }
  html, body {
    margin: 0;
    padding: 0;
    overflow: hidden;
    background: #ffffff;
  }
  .banner {
    position: relative;
    width: 1200px;
    height: 162px;
    overflow: hidden;
    font-family: "Oswald", "Arial Narrow", sans-serif;
  }
  .banner__shapes {
    position: absolute;
    inset: 0;
  }
  .step-number {
    font-family: "Oswald", "Arial Narrow", sans-serif;
    font-weight: 500;
    font-size: 62px;
    fill: var(--number);
  }
  .step-number--active { fill: var(--yellow-light); }
  .step-text {
    position: absolute;
    top: 4px;
    margin: 0;
    font-weight: 500;
    font-size: 31px;
    line-height: 33px;
    text-transform: uppercase;
    letter-spacing: 0.2px;
    color: var(--text-light);
  }
  .step-text--one { left: 188px; }
  .step-text--two { left: 537px; color: var(--text-dark); }
  .step-text--three { left: 911px; }
  .brand {
    position: absolute;
    right: 10px;
    bottom: 8px;
    display: flex;
    align-items: center;
    gap: 6px;
    font-weight: 600;
    font-size: 24px;
    line-height: 1;
    color: var(--text-dark);
  }
  .brand__mark {
    width: 16px;
    height: 16px;
    background: var(--yellow);
  }
</style>
</head>
<body>
<div class="banner">
  <svg class="banner__shapes" width="1200" height="162" viewBox="0 0 1200 162" aria-hidden="true">
    <!-- backdrop and floor -->
    <rect x="0" y="0" width="1200" height="162" fill="var(--bg-dark)"/>
    <rect x="0" y="128" width="1200" height="34" fill="var(--floor)"/>
    <polygon points="0,128 1200,128 1200,162 0,162" fill="var(--floor-light)" opacity="0.35"/>

    <!-- step panels -->
    <polygon points="0,0 360,0 360,128 0,128" fill="var(--panel-dark)"/>
    <polygon points="360,0 740,0 700,128 360,128" fill="var(--panel-mid)" opacity="0.6"/>
    <polygon points="400,0 770,0 735,128 370,128" fill="var(--yellow)"/>
    <polygon points="400,0 770,0 760,30 405,30" fill="var(--yellow-light)" opacity="0.5"/>
    <polygon points="770,0 1200,0 1200,128 735,128" fill="var(--panel-mid)"/>

    <!-- cube 1 -->
    <g class="cube">
      <polygon points="20,58 40,40 142,40 122,58" fill="var(--cube-top)"/>
      <polygon points="122,58 142,40 142,150 122,162" fill="var(--cube-side)"/>
      <rect x="20" y="58" width="102" height="104" fill="var(--cube-front)"/>
      <text class="step-number" x="71" y="135" text-anchor="middle">1</text>
    </g>

    <!-- cube 2 -->
    <g class="cube cube--active">
      <polygon points="372,58 392,40 494,40 474,58" fill="var(--yellow-light)"/>
      <polygon points="474,58 494,40 494,150 474,162" fill="var(--yellow-deep)"/>
      <rect x="372" y="58" width="102" height="104" fill="var(--yellow)"/>
      <text class="step-number step-number--active" x="423" y="135" text-anchor="middle">2</text>
    </g>

    <!-- cube 3 -->
    <g class="cube">
      <polygon points="742,58 762,40 864,40 844,58" fill="var(--cube-top)"/>
      <polygon points="844,58 864,40 864,150 844,162" fill="var(--cube-side)"/>
      <rect x="742" y="58" width="102" height="104" fill="var(--cube-front)"/>
      <text class="step-number" x="793" y="135" text-anchor="middle">3</text>
    </g>
  </svg>

  <p class="step-text step-text--one">Register an<br>account.</p>
  <p class="step-text step-text--two">Purchase<br>the starter<br>package.</p>
  <p class="step-text step-text--three">Start bidding<br>and save up<br>to 98% off!</p>

  <div class="brand">
    <span class="brand__mark"></span>
    <span class="brand__name">ZelNork</span>
  </div>
</div>
</body>
</html>
```